Plumbing Business Card Design

our business is a plumbing business.
we would like to see designs with our LOGO featured and then either purple or black writing with a white back ground
or black back ground with white or purple writing or even a purple card!
one option we would love to see is if you could get the KTW letters away from the white background ( it is currently in a white box as a jpeg )it is currently on and overlay it onto black.
FRONT
KTW image to be displayed on the front, please use the attached picture. ( you can remove the email address and mobile number from the botttom and re write it in different font or in a different place on the front.
Directly under the large KTW we would like the words Copper Linton Plumbing.
could be spread out like this C O P P E R L I N T O N
P L U M B I N G
We really are open to suggestions though!
Also on the front of the card we could like our little catch phrase somewhere Borra's Trusted Plumber

we dont want in plumbing pictures or photos but we are open to swirl across the card or water movement or droplets.

BACK
These services need to be dot pointed or listed on the back
Hot & Cold Water Services
Gas Fitting
Bathroom & Kitchen Renovations
Metal Roofing & Guttering
New Homes & Extensions
Hot Water Service Changeovers
Drainage & Stormwater Works
All General Plumbing & Maitenance

in smaller writing or down the bottom of the card on the back please display write this Lic. No 492318

Contact Information for Business Card

Reid Linton
Mobile: 0427 316 902
email: copperlintonplumbing@mailvane.example
FInd Us on Facebook Copper Linton Plumbing ( with the f symbol ) either on the front or the back

```html
<!DOCTYPE html>
<html lang="en">
<head>
<meta charset="utf-8">
<title>Copper Linton Plumbing – Business Card</title>
<link rel="stylesheet" href="https://fonts.googleapis.com/css2?family=Open+Sans:wght@400;600;700&display=swap">
<style>
  :root {
    --backdrop: #1c1c1f;
    --card: #f4f5f8;
    --ink: #1d1d22;
    --purple: #5a3fa3;
    --purple-deep: #4c3392;
    --blue: #5b88c9;
    --blue-soft: #6f97d2;
    --drop: #3f7fd1;
  }
  * { margin: 0; padding: 0; box-sizing: border-box; }
  html, body {
    width: 1200px; height: 800px; overflow: hidden;
    background: var(--backdrop);
    font-family: "Open Sans", Arial, sans-serif;
  }
  .stage { position: relative; width: 1200px; height: 800px; }
  .card {
    position: absolute;
    width: 560px; height: 342px;
    background: var(--card);
    overflow: hidden;
  }
  .card--back { left: 30px; top: 229px; }
  .card--front { left: 610px; top: 229px; }

  .brand {
    position: absolute;
    text-align: center;
    color: var(--blue);
    font-weight: 700;
  }
  .brand__mark { display: block; line-height: 1; letter-spacing: 4px; }
  .brand__name { display: block; letter-spacing: 0.5px; white-space: nowrap; }
  .card--front .brand { right: 30px; top: 36px; width: 240px; }
  .card--front .brand__mark { font-size: 76px; }
  .card--front .brand__name { font-size: 15px; margin-top: 8px; }
  .card--back .brand { right: 24px; bottom: 26px; width: 200px; }
  .card--back .brand__mark { font-size: 60px; }
  .card--back .brand__name { font-size: 12.5px; margin-top: 6px; }

  .services {
    position: absolute; left: 34px; top: 28px;
    list-style: none;
  }
  .services__item {
    display: flex; align-items: center; gap: 12px;
    font-size: 16px; color: var(--ink);
    height: 29px;
  }
  .services__icon { width: 14px; height: 18px; flex: none; }

  .holder {
    position: absolute; left: 38px; top: 128px;
    font-size: 27px; font-weight: 600; color: var(--purple);
    letter-spacing: 0.5px;
  }
  .divider {
    position: absolute; left: 34px; right: 40px; top: 180px;
    height: 1px; background: var(--ink);
  }
  .contacts {
    position: absolute; left: 38px; top: 196px;
    list-style: none;
  }
  .contacts__item {
    display: flex; align-items: center; gap: 14px;
    height: 29px; font-size: 17px; color: var(--ink);
  }
  .contacts__icon {
    width: 16px; height: 16px; flex: none;
    background: var(--purple); border-radius: 2px;
    display: flex; align-items: center; justify-content: center;
  }
  .contacts__icon svg { width: 11px; height: 11px; }

  .bands {
    position: absolute; left: 0; bottom: 0;
    width: 560px; height: 58px;
  }
</style>
</head>
<body>
<main class="stage">

  <section class="card card--back" aria-label="Business card back">
    <ul class="services">
      <li class="services__item"><svg class="services__icon" viewBox="0 0 14 18"><path d="M7 1 C7 1 1 8 1 12 a6 6 0 0 0 12 0 C13 8 7 1 7 1z" fill="var(--drop)"/></svg>Hot &amp; Cold Water Services</li>
      <li class="services__item"><svg class="services__icon" viewBox="0 0 14 18"><path d="M7 1 C7 1 1 8 1 12 a6 6 0 0 0 12 0 C13 8 7 1 7 1z" fill="var(--drop)"/></svg>Gas Fitting</li>
      <li class="services__item"><svg class="services__icon" viewBox="0 0 14 18"><path d="M7 1 C7 1 1 8 1 12 a6 6 0 0 0 12 0 C13 8 7 1 7 1z" fill="var(--drop)"/></svg>Bathroom &amp; Kitchen Renovations</li>
      <li class="services__item"><svg class="services__icon" viewBox="0 0 14 18"><path d="M7 1 C7 1 1 8 1 12 a6 6 0 0 0 12 0 C13 8 7 1 7 1z" fill="var(--drop)"/></svg>Metal Roofing &amp; Guttering</li>
      <li class="services__item"><svg class="services__icon" viewBox="0 0 14 18"><path d="M7 1 C7 1 1 8 1 12 a6 6 0 0 0 12 0 C13 8 7 1 7 1z" fill="var(--drop)"/></svg>New Homes &amp; Extensions</li>
      <li class="services__item"><svg class="services__icon" viewBox="0 0 14 18"><path d="M7 1 C7 1 1 8 1 12 a6 6 0 0 0 12 0 C13 8 7 1 7 1z" fill="var(--drop)"/></svg>Hot Water Service Changeovers</li>
      <li class="services__item"><svg class="services__icon" viewBox="0 0 14 18"><path d="M7 1 C7 1 1 8 1 12 a6 6 0 0 0 12 0 C13 8 7 1 7 1z" fill="var(--drop)"/></svg>Drainage &amp; Stormwater Works</li>
      <li class="services__item"><svg class="services__icon" viewBox="0 0 14 18"><path d="M7 1 C7 1 1 8 1 12 a6 6 0 0 0 12 0 C13 8 7 1 7 1z" fill="var(--drop)"/></svg>All General Plumbing &amp; Maitenance</li>
    </ul>
    <div class="brand">
      <span class="brand__mark">KTW</span>
      <span class="brand__name">COPPER LINTON PLUMBING</span>
    </div>
  </section>

  <section class="card card--front" aria-label="Business card front">
    <div class="brand">
      <span class="brand__mark">KTW</span>
      <span class="brand__name">COPPER LINTON PLUMBING</span>
    </div>

    <h1 class="holder">Reid Linton</h1>
    <div class="divider"></div>

    <ul class="contacts">
      <li class="contacts__item">
        <span class="contacts__icon"><svg viewBox="0 0 12 12"><path d="M3 1 L5 3.5 L4 5 C4.8 6.6 5.6 7.4 7 8 L8.5 7 L11 9 L10 11 C5.5 11 1 6.5 1 2z" fill="#fff"/></svg></span>
        0427 316 902
      </li>
      <li class="contacts__item">
        <span class="contacts__icon"></span>
        Copper Linton Plumbing
      </li>
      <li class="contacts__item">
        <span class="contacts__icon"><svg viewBox="0 0 12 12"><rect x="1" y="2.5" width="10" height="7" fill="none" stroke="#fff" stroke-width="1.2"/><path d="M1 2.5 L6 7 L11 2.5" fill="none" stroke="#fff" stroke-width="1.2"/></svg></span>
        copperlintonplumbing@mailvane.example
      </li>
    </ul>

    <svg class="bands" viewBox="0 0 560 58" preserveAspectRatio="none" aria-hidden="true">
      <polygon points="0,2 300,16 560,16 560,58 0,58" fill="var(--purple-deep)"/>
      <polygon points="0,0 292,13 292,13 0,4" fill="var(--purple)"/>
      <polygon points="0,6 290,19 308,58 0,58" fill="var(--blue-soft)"/>
    </svg>
  </section>

</main>
</body>
</html>
```